Business Card Design - Crisp & Clean

Looking for a new clean and crisp business card design. Design must incorporate our corporate colors (see attached style sheet). We're a pretty fun loving group who likes to keep it light while still portraying a professional image. Card should incorporate both our logo and our mascot (see attachment). Card should be double sided and should have room for our social media - Gleamrow, Brisk Hub and Zumbly on the back. Font selections do not have to match the style guide.

```html
<!DOCTYPE html>
<html lang="en">
<head>
<meta charset="utf-8">
<title>BrightPeople Business Cards</title>
<link href="https://fonts.googleapis.com/css2?family=Open+Sans:wght@400;600;800&display=swap" rel="stylesheet">
<style>
  :root {
    --backdrop: #ebe8e4;
    --card-white: #f7f7f6;
    --card-blue: #4a73b9;
    --brand-yellow: #f2b31b;
    --brand-yellow-light: #f7cf55;
    --brand-yellow-fade: rgba(242,179,27,0);
    --ink: #1d1d1b;
    --ink-soft: #3a3a3a;
    --social-blue: #4a73b9;
    --text-on-blue: #f2f4f8;
    --name-on-blue: #f6d35a;
  }
  * { box-sizing: border-box; margin: 0; padding: 0; }
  html, body {
    width: 1200px; height: 997px; overflow: hidden;
    background: var(--backdrop);
    font-family: "Open Sans", Arial, sans-serif;
  }
  .stage { position: relative; width: 1200px; height: 997px; }

  .card {
    position: absolute;
    width: 560px; height: 320px;
    border-radius: 4px;
    box-shadow: 0 6px 18px rgba(0,0,0,0.12);
    overflow: hidden;
  }

  /* Front card */
  .card-front { left: 60px; top: 170px; background: var(--card-white); }
  .brand {
    position: absolute; left: 70px; top: 92px;
    display: flex; align-items: center; gap: 18px;
  }
  .brand-dot {
    width: 56px; height: 56px; border-radius: 50%;
    background: var(--brand-yellow);
  }
  .brand-name {
    font-weight: 800; font-size: 40px; color: var(--ink);
    letter-spacing: -0.5px; line-height: 1;
  }
  .brand-tagline {
    font-weight: 800; font-size: 11.5px; color: var(--ink);
    letter-spacing: 0.4px; margin-top: 5px;
  }
  .social-row {
    position: absolute; left: 26px; right: 26px; bottom: 28px;
    display: flex; justify-content: space-between;
    font-size: 12.5px; color: var(--ink-soft); white-space: nowrap;
  }
  .social-item { display: flex; align-items: center; gap: 6px; }
  .social-mark {
    width: 13px; height: 13px; border-radius: 2px;
    background: var(--social-blue); flex: none;
  }

  /* Back card */
  .card-back { left: 580px; top: 500px; background: var(--card-blue); }
  .mascot-art {
    position: absolute; left: 30px; top: 40px;
    width: 270px; height: 260px;
    background: radial-gradient(circle closest-side at 50% 50%,
      var(--brand-yellow-light) 0%,
      var(--brand-yellow) 45%,
      var(--brand-yellow-fade) 100%);
  }
  .contact {
    position: absolute; left: 320px; top: 58px;
    color: var(--text-on-blue); font-size: 13px; line-height: 1.35;
    white-space: nowrap;
  }
  .contact-name { color: var(--name-on-blue); font-weight: 600; font-size: 14px; }
  .contact-title { font-weight: 600; margin-bottom: 14px; }
  .contact-lines { margin-bottom: 14px; }
</style>
</head>
<body>
<main class="stage">
  <section class="card card-front" aria-label="Card front">
    <div class="brand">
      <span class="brand-dot"></span>
      <div>
        <div class="brand-name">BrightPeople</div>
        <div class="brand-tagline">HR PROCESS MANAGEMENT SOLUTIONS</div>
      </div>
    </div>
    <div class="social-row">
      <span class="social-item" aria-label="Gleamrow"><span class="social-mark"></span>/ItsBrightPeople</span>
      <span class="social-item" aria-label="Brisk Hub"><span class="social-mark"></span>/brightpeople-hr-process-management</span>
      <span class="social-item" aria-label="Zumbly"><span class="social-mark"></span>/ItsBrightPeople</span>
    </div>
  </section>

  <section class="card card-back" aria-label="Card back">
    <div class="mascot-art" role="img" aria-label="Company mascot holding a light bulb among yellow brand swirls"></div>
    <div class="contact">
      <div class="contact-name">Dale Whitmore</div>
      <div class="contact-title">Company founder &amp; CEO</div>
      <div class="contact-lines">
        mobile 555.014.2290<br>
        dale@brightpeople.com<br>
        www.brightpeople.com
      </div>
      <div>
        48 Harbor Lane<br>
        Marlow, TX 70000<br>
        United States
      </div>
    </div>
  </section>
</main>
</body>
</html>
```